318 Diamond & Fastpitch Clinic 2017

Design a flyer that will promote our 2017 summer camp for boys and girls softball.

Weeks of
July 10th - 14th
July 17th - 21st.

Players ages 5 - 11.
Full day = 9:30am - 2:30pm half day = 9:30am - 11:30am.
$295 / full day : $195/ half day

Hosted by "318 Diamond" affiliated with the KV Meteors Touring Baseball & Softball Club and the Pine Hollow Junior League,

Camp Location PHJL, Lane 48C Maple Bluff.

PHone 555-284-7730, email info@318diamond.example

The color should be "Red white and blue color scheme" with dates and location standing out. 318 Logo should be prominent PHJL and Meteors smaller and secondary.

Feel free to use stock photo's if available. visit www.kvmeteors.example for more pictures and there are links for the 2017 summer camp there with possibly some more information.

Target Market(s)

to catch the eye of parents of players ages 5 - 11 already at little league or shopping in local stores

Colors
ec1f27
0355a3
ffffff

Requirements
Must have
• red white and blue design,
• 318 logo and summer camp prominent so it catches the eye and explains what it is right away.
• the meteors and pine hollow logo's a the bottom showing the affiliation.
Nice to have
• stock photo's or something showing players having a great time or a beautiful ballpark
Should not have
• to much clutter or hard to figure out what it's for

```html
<!DOCTYPE html>
<html lang="en">
<head>
<meta charset="utf-8">
<title>318 Diamond &amp; Fastpitch Clinic 2017 – Summer Camp</title>
<link href="https://fonts.googleapis.com/css2?family=Oswald:wght@400;500;700&family=Roboto+Condensed:wght@400;700&display=swap" rel="stylesheet">
<style>
  :root {
    --red: #ec1f27;
    --blue: #0355a3;
    --white: #ffffff;
    --paper: #f1f2f4;
    --ink: #1c2a44;
  }
  html, body { margin: 0; padding: 0; overflow: hidden; }
  body { width: 847px; height: 1200px; background: var(--paper); }
  .flyer {
    position: relative;
    width: 847px; height: 1200px;
    overflow: hidden;
    background: var(--paper);
    font-family: "Roboto Condensed", "Arial Narrow", sans-serif;
    color: var(--white);
  }
  .panels { position: absolute; inset: 0; }
  .corner-decor {
    position: absolute; left: 0; top: 0; width: 360px; height: 260px;
    background: radial-gradient(ellipse at 30% 35%, rgba(236,31,39,.35), rgba(236,31,39,0) 70%);
  }
  .player-photo {
    position: absolute; left: 0; top: 110px; width: 560px; height: 830px;
    background: linear-gradient(160deg, #d9dde3 0%, #c7cbd2 30%, #caa48a 52%, #e9e9ec 70%, #b9c0cb 100%);
    clip-path: polygon(0 0, 100% 0, 88% 100%, 0 100%);
  }
  .headline {
    position: absolute; right: 38px; top: 36px; margin: 0;
    text-align: right;
    font-family: "Oswald", "Arial Narrow", sans-serif;
    font-weight: 700; text-transform: uppercase;
    line-height: .95; letter-spacing: 1px;
  }
  .headline .year { font-size: 78px; display: block; }
  .headline .word { font-size: 96px; display: block; }
  .dates {
    position: absolute; right: 38px; top: 405px;
    text-align: right;
    font-family: "Oswald", "Arial Narrow", sans-serif;
    font-weight: 700; font-size: 58px; line-height: 1.02;
    text-transform: uppercase;
  }
  .dates-arrow { position: absolute; left: 508px; top: 486px; }
  .location {
    position: absolute; left: 548px; top: 600px; width: 262px;
    background: var(--red); padding: 10px 12px;
    font-size: 18px; line-height: 1.25;
  }
  .details {
    position: absolute; right: 38px; top: 694px; width: 300px;
    text-align: right; font-size: 21px; line-height: 1.3;
  }
  .details p { margin: 0; }
  .details .ages { margin-bottom: 8px; }
  .contact {
    position: absolute; right: 38px; top: 850px;
    text-align: right; font-size: 17px; line-height: 1.35;
  }
  .brand {
    position: absolute; left: 60px; top: 960px;
    display: flex; align-items: center; gap: 16px;
  }
  .brand-mark { width: 46px; height: 46px; border-radius: 50%; background: var(--red); }
  .brand-name {
    font-family: "Oswald", "Arial Narrow", sans-serif;
    font-weight: 700; font-size: 150px; line-height: 1;
    color: var(--blue);
  }
  .brand-sub {
    position: absolute; left: 72px; top: 1130px;
    font-family: "Oswald", "Arial Narrow", sans-serif;
    font-weight: 700; font-size: 26px; letter-spacing: 2px;
    color: var(--blue); text-transform: uppercase;
  }
  .partners {
    position: absolute; left: 578px; top: 955px;
    display: flex; gap: 30px; align-items: center;
  }
  .partner-badge { width: 100px; height: 64px; background: var(--blue); }
  .partner-badge.round { width: 70px; height: 70px; border-radius: 50%; background: #3a9a3f; }
  .hosted {
    position: absolute; left: 552px; top: 1048px; width: 260px; margin: 0;
    font-size: 13px; line-height: 1.35; color: var(--ink);
  }
</style>
</head>
<body>
<main class="flyer">
  <svg class="panels" width="847" height="1200" viewBox="0 0 847 1200" aria-hidden="true">
    <polygon points="470,0 847,0 847,940 420,940" fill="var(--blue)"/>
    <polygon points="430,0 847,0 847,270 400,300" fill="var(--red)"/>
  </svg>

  <div class="corner-decor" role="img" aria-label="Decorative red baseballs"></div>
  <div class="player-photo" role="img" aria-label="Photo of a young softball player in a batting helmet, ready to swing"></div>

  <h1 class="headline">
    <span class="year">2017</span>
    <span class="word">Summer</span>
    <span class="word">Camp</span>
  </h1>

  <svg class="dates-arrow" width="20" height="40" viewBox="0 0 20 40" aria-hidden="true">
    <polyline points="18,2 3,20 18,38" fill="none" stroke="var(--red)" stroke-width="4"/>
  </svg>
  <div class="dates">
    July<br>10th-14th<br>17th-21st
  </div>

  <div class="location">Camp Location PHJL,<br>Lane 48C Maple Bluff.</div>

  <div class="details">
    <p class="ages">Players ages 5 - 11</p>
    <p>Full day - 9:30am - 2:30pm</p>
    <p>half day - 9:30am - 11:30am</p>
    <p>$295 / full day : $195/ half day</p>
  </div>

  <div class="contact">
    Phone 555-284-7730<br>
    email : info@318diamond.example
  </div>

  <div class="brand">
    <span class="brand-mark"></span>
    <span class="brand-name">318</span>
  </div>
  <div class="brand-sub">Diamond &amp; Fastpitch</div>

  <div class="partners">
    <div class="partner-badge" role="img" aria-label="KV Meteors club badge"></div>
    <div class="partner-badge round" role="img" aria-label="Pine Hollow Junior League badge"></div>
  </div>

  <p class="hosted">Hosted by "318 Diamond" affiliated with the KV Meteors Touring Baseball &amp; Softball Club and the Pine Hollow Junior League</p>
</main>
</body>
</html>
```